Web Design Project - Vextrion

We have created an initial website at http://www.vextrion-example.com

This project requires you to take the current website and redesigning it to improve the overall look and feel.

Feel free to experiment with everything including:

~ colour schemes
~ layout

The only constraints are

- the text content
- the app icons on /games
- the logo structure (feel free to change the colour schemes / logo image)

In terms of process - please feel free to post concepts / mockups for one page - if this is easier for you to do quickly (without revamping the entire site).

As well as the website, please provide designs for a facebook page cover and profile picture for http://www.socialpage-example.com/pages/Vextrion/730194652018364

Thanks for the submissions - but we've not quite found what we're looking for.

This site is on which appeals to us - please use this for inspiration: http://brambury-example.com/

Thanks

Reason: I am about to make this project "guaranteed" and want to give more time to submit

Please submit your creative ideas - we look forward to receiving them.

Reason: Hi, Deadline extended so that we can see revisions Thanks

Target Market(s)

Marketing Executives / CEOs of Media Companies

Industry/Entity Type

Games

```html
<!DOCTYPE html>
<html lang="en">
<head>
<meta charset="utf-8">
<title>Vextrion – In-play second screen games</title>
<link rel="stylesheet" href="https://fonts.googleapis.com/css2?family=Ubuntu:ital,wght@0,300;0,400;0,500;0,700;1,400&family=Arimo:ital,wght@0,400;0,700;1,400&display=swap">
<style>
  :root {
    --ink: #111111;
    --green: #19c81b;
    --green-dark: #0fa010;
    --blue: #1a6fe0;
    --blue-dark: #0d55bd;
    --red: #e2361a;
    --red-dark: #bf2408;
    --link-blue: #4a6aa8;
    --body-grey: #6a6a6a;
    --nav-bg: #161616;
    --menu-bg: #0c3a4c;
    --footer-bg: #383838;
    --footer-text: #e6e6e6;
    --tagline: #222222;
    --accent-red: #d11a1a;
  }
  * { box-sizing: border-box; margin: 0; padding: 0; }
  html, body { width: 918px; height: 1200px; overflow: hidden; background: #fff; }
  body { position: relative; font-family: "Ubuntu", sans-serif; color: var(--ink); }
  .top-rule { position: absolute; left: 0; top: 5px; width: 918px; height: 4px; background: var(--ink); }

  .brand { position: absolute; left: 44px; top: 81px; display: flex; align-items: center; gap: 8px; }
  .brand-mark { width: 24px; height: 24px; background: var(--green); }
  .brand-name { font-family: "Ubuntu", sans-serif; font-weight: 700; font-size: 24px; line-height: 30px; color: var(--green); }

  .tagline { position: absolute; left: 188px; top: 86px; font-family: "Arimo", sans-serif; font-style: italic; font-size: 17px; color: var(--tagline); white-space: nowrap; }

  .follow-top { position: absolute; left: 756px; top: 44px; display: flex; align-items: center; gap: 7px; font-family: "Arimo", sans-serif; font-size: 11px; color: var(--accent-red); text-decoration: none; }
  .follow-top .dot { width: 16px; height: 16px; border-radius: 50%; background: #29a9e1; }

  .search { position: absolute; left: 693px; top: 138px; width: 189px; height: 19px; border: 1px solid #d8d8d8; font-family: "Arimo", sans-serif; font-size: 11px; color: #999; padding: 3px 7px; }
  .search svg { position: absolute; right: 5px; top: 3px; }

  .main-nav { position: absolute; left: 36px; top: 179px; width: 846px; height: 44px; background: linear-gradient(#2b2b2b, var(--nav-bg) 45%, #050505); border: 3px solid #000; }
  .main-nav a { position: absolute; top: 13px; transform: translateX(-50%); font-family: "Ubuntu", sans-serif; font-weight: 500; font-size: 12px; color: #fff; text-decoration: none; white-space: nowrap; }
  .main-nav a.is-open { color: #9aa3aa; }

  .hero { position: absolute; left: 36px; top: 226px; width: 846px; height: 323px; background: linear-gradient(#1aa2e0 0%, #6ad0f2 35%, #2f2f2f 52%, #3fae2a 60%, #5fd53a 100%); }

  .dropdown { position: absolute; left: 567px; top: 223px; width: 144px; }
  .dropdown .bar { height: 3px; background: #9aa3aa; }
  .dropdown a { display: block; height: 28px; line-height: 28px; padding-left: 14px; background: var(--menu-bg); border-bottom: 1px solid #1f5a70; font-family: "Ubuntu", sans-serif; font-weight: 500; font-size: 11px; letter-spacing: .5px; color: #fff; text-decoration: none; }

  .slider-dots { position: absolute; top: 558px; left: 0; width: 918px; display: flex; justify-content: center; gap: 5px; }
  .slider-dots span { width: 18px; height: 18px; border-radius: 50%; background: var(--blue); border: 1px solid #0a3f8f; }
  .slider-dots span.active { background: var(--green); border-color: #0b7a0c; }

  .feature { position: absolute; top: 586px; width: 252px; }
  .feature-head { height: 35px; padding-left: 10px; line-height: 33px; color: #fff; font-weight: 700; font-size: 13.5px; border: 2px solid; }
  .feature h3 { margin: 20px 0 0 10px; font-weight: 500; font-size: 14px; color: var(--link-blue); }
  .feature p { margin: 12px 0 0 9px; width: 222px; font-weight: 300; font-size: 11.5px; line-height: 16px; color: var(--body-grey); }
  .feature .more { display: block; margin: 14px 0 0 10px; width: 90px; height: 21px; line-height: 19px; text-align: center; color: #fff; font-weight: 500; font-size: 11px; text-decoration: none; border: 1px solid; }
  .feature.green .feature-head, .feature.green .more { background: linear-gradient(var(--green), var(--green-dark)); border-color: #0d8f0e; }
  .feature.blue .feature-head, .feature.blue .more { background: linear-gradient(var(--blue), var(--blue-dark)); border-color: #0b4ea9; }
  .feature.red .feature-head, .feature.red .more { background: linear-gradient(var(--red), var(--red-dark)); border-color: #a51d06; }

  .audiences { position: absolute; left: 36px; top: 787px; width: 846px; height: 60px; background: linear-gradient(#ececec, #fff); }
  .audience { position: absolute; top: 812px; width: 440px; font-family: "Arimo", sans-serif; }
  .audience h2 { font-size: 13.5px; font-weight: 700; color: #222; white-space: nowrap; }
  .audience ul { list-style: none; margin-top: 16px; width: 400px; }
  .audience li { font-style: italic; font-size: 13.5px; line-height: 20px; color: #333; }

  .site-footer { position: absolute; left: 36px; top: 1038px; width: 846px; height: 144px; background: var(--footer-bg); color: var(--footer-text); font-family: "Arimo", sans-serif; }
  .legal { position: absolute; left: 0; top: 54px; width: 675px; text-align: center; }
  .legal strong { display: block; font-size: 12.5px; }
  .legal small { display: block; margin-top: 6px; font-size: 11px; color: #cfcfcf; }
  .footer-divider { position: absolute; left: 675px; top: 20px; width: 1px; height: 110px; background: #555; }
  .follow { position: absolute; left: 700px; top: 25px; font-size: 11.5px; }
  .social { display: flex; gap: 6px; margin-top: 8px; }
  .social span { width: 20px; height: 20px; border-radius: 50%; }
  .footer-links { list-style: none; margin-top: 11px; }
  .footer-links li { font-size: 11.5px; line-height: 26px; }
  .footer-links li::before { content: "▸"; font-size: 8px; margin-right: 5px; vertical-align: 2px; }
</style>
</head>
<body>
  <div class="top-rule"></div>

  <header>
    <div class="brand"><span class="brand-mark"></span><span class="brand-name">Vextrion</span></div>
    <p class="tagline">Delivering in-play second screen games based on live broadcast events</p>
    <a class="follow-top" href="#"><span class="dot"></span>Follow us on Chatterline</a>
    <div class="search">Search
      <svg width="13" height="13" viewBox="0 0 13 13"><circle cx="8" cy="5" r="4" fill="none" stroke="#aaa" stroke-width="1.3"/><line x1="5" y1="8" x2="1" y2="12" stroke="#aaa" stroke-width="1.5"/></svg>
    </div>
  </header>

  <nav class="main-nav">
    <a href="#" style="left:191px">HOME</a>
    <a href="#" style="left:275px">ABOUT</a>
    <a href="#" style="left:360px">GAMES</a>
    <a href="#" style="left:459px">SOLUTIONS</a>
    <a href="#" class="is-open" style="left:551px">UPDATE</a>
    <a href="#" style="left:645px">CONTACT</a>
  </nav>

  <div class="hero" role="img" aria-label="Illustration of a footballer striking the ball past a diving goalkeeper in a floodlit stadium"></div>

  <div class="dropdown">
    <div class="bar"></div>
    <a href="#">Reformidans</a>
    <a href="#">Iuvaret</a>
    <a href="#">Consequuntur</a>
    <a href="#">Ullamcorper</a>
    <a href="#">Essent</a>
    <a href="#">Gloriatur</a>
  </div>

  <div class="slider-dots"><span class="active"></span><span></span><span></span><span></span><span></span></div>

  <section class="feature green" style="left:36px">
    <div class="feature-head">Partem Similique</div>
    <h3>Liber quodsi</h3>
    <p>Quo agam facilisis ei, liber quodsi debitis ex est. Labore audire eam in. Case facilisi eleifend te pri, mei ei exerci oportere. Per an ignota postea. Ea duo fugit augue</p>
    <a class="more" href="#">Read more</a>
  </section>
  <section class="feature blue" style="left:333px">
    <div class="feature-head">Partem Similique</div>
    <h3>Liber quodsi</h3>
    <p>Quo agam facilisis ei, liber quodsi debitis ex est. Labore audire eam in. Case facilisi eleifend te pri, mei ei exerci oportere. Per an ignota postea. Ea duo fugit augue</p>
    <a class="more" href="#">Read more</a>
  </section>
  <section class="feature red" style="left:630px">
    <div class="feature-head">Partem Similique</div>
    <h3>Liber quodsi</h3>
    <p>Quo agam facilisis ei, liber quodsi debitis ex est. Labore audire eam in. Case facilisi eleifend te pri, mei ei exerci oportere. Per an ignota postea. Ea duo fugit augue</p>
    <a class="more" href="#">Read more</a>
  </section>

  <div class="audiences"></div>
  <section class="audience" style="left:45px">
    <h2>For Media Owners, Broadcasters or Sponsors of Live Events</h2>
    <ul>
      <li>Games can be re-skinned &amp; launched for your live event</li>
      <li>Increases value of live media rights through increased viewer engagement</li>
      <li>Games capture extensive customer data to enhance your CRM capabilities</li>
      <li>Deep social network integration and social gameplay mechanisms maximise chances of the game "going viral"</li>
      <li>Click here to find out more about our Solutions</li>
    </ul>
  </section>
  <section class="audience" style="left:500px">
    <h2>For Game Players and Fans</h2>
    <ul>
      <li>Play games with friends while watching live events</li>
      <li>Real-time gameplay based on the event you're watching</li>
      <li>Compete against your friends and other players</li>
      <li>Free to play prizes for the best performing games</li>
      <li>Click here to see a list of our games</li>
    </ul>
  </section>

  <footer class="site-footer">
    <div class="legal">
      <strong>Use of this Web site constitutes acceptance of Vextrion's Terms of Service and Privacy Policy</strong>
      <small>© Copyright 2012. All rights reserved.</small>
    </div>
    <div class="footer-divider"></div>
    <div class="follow">
      Follow us:
      <div class="social">
        <span style="background:#f08a1c"></span>
        <span style="background:#3db7e8"></span>
        <span style="background:#2b4f9a"></span>
        <span style="background:#9a9a9a"></span>
      </div>
      <ul class="footer-links">
        <li>Terms and Conditions</li>
        <li>Privacy Policy</li>
      </ul>
    </div>
  </footer>
</body>
</html>
```